Party planning business card design

Galas with Wren is a party planning business

Function Planning: Weddings/Themed Parties/Children's Parties

Adult and Children's Photo Booths
Party Themed boxes,
We can find the venue, entertainment. face painters.

Children's costumes and accessories - Sell / Hire

Web: www.galaswithwren.example
Facebook: Galas with Wren

Industry/Entity Type

Party Planning

Contact Information for Business Card

Galas With Wren, Rosalind Pektrew,
Creative Director

Colors
e34297
000000

Requirements
Must have
• on my logo are you able to edit the stars to pink?

```html
<!DOCTYPE html>
<html lang="en">
<head>
<meta charset="utf-8">
<title>Galas with Wren — Business Card</title>
<link rel="stylesheet" href="https://fonts.googleapis.com/css2?family=Fira+Sans+Condensed:ital,wght@0,400;0,500;1,400&display=swap">
<style>
  :root {
    --canvas: #ffffff;
    --pink: #e34297;
    --pink-soft: #e85aa4;
    --pink-light: #f07cc0;
    --plum-deep: #3f1131;
    --plum-dark: #1f1419;
    --ink: #000000;
    --text-light: #f4eef2;
    --logo-text: #ece3e8;
  }
  * { box-sizing: border-box; margin: 0; padding: 0; }
  html, body {
    width: 1200px; height: 741px; overflow: hidden;
    background: var(--canvas);
    font-family: "Fira Sans Condensed", "Arial Narrow", sans-serif;
  }
  .canvas { position: relative; width: 1200px; height: 741px; }

  .card {
    position: absolute; top: 264px;
    width: 366px; height: 209px;
    border: 1px solid var(--ink);
    overflow: hidden;
  }

  /* Front */
  .card--front { left: 166px; background: var(--pink); }
  .card__stars {
    position: absolute; inset: 0;
    background:
      radial-gradient(ellipse 55% 40% at 40% 10%, rgba(205, 40, 130, 0.35), transparent 70%),
      linear-gradient(115deg, rgba(240, 110, 180, 0.25) 0%, transparent 45%, rgba(205, 45, 135, 0.3) 100%);
  }
  .card__brand {
    position: absolute; left: 12px; bottom: 18px;
    font-size: 40px; font-weight: 400; letter-spacing: -0.5px;
    color: var(--logo-text);
    line-height: 1;
  }

  /* Back */
  .card--back {
    left: 682px;
    background: linear-gradient(135deg, var(--plum-deep) 0%, #2c1224 45%, var(--plum-dark) 100%);
    color: var(--text-light);
    text-align: center;
  }
  .person__name { position: absolute; top: 17px; width: 100%; font-size: 19px; font-weight: 400; }
  .person__title { position: absolute; top: 44px; width: 100%; font-size: 14px; font-style: italic; color: var(--pink-light); }
  .divider {
    position: absolute; top: 72px; left: 36px; right: 36px; height: 1px;
    background: linear-gradient(90deg, transparent, var(--pink) 50%, transparent);
  }
  .contact {
    position: absolute; left: 110px; top: 100px;
    list-style: none; text-align: left;
  }
  .contact__item {
    display: flex; align-items: center; gap: 9px;
    height: 25.5px;
    font-size: 14.5px; font-style: italic;
  }
  .contact__icon { width: 12px; height: 12px; flex: none; }
</style>
</head>
<body>
<main class="canvas">
  <section class="card card--front" aria-label="Card front">
    <div class="card__stars" role="img" aria-label="Faint scattered pink star pattern"></div>
    <p class="card__brand">Galas with Wren</p>
  </section>

  <section class="card card--back" aria-label="Card back">
    <h1 class="person__name">Rosalind Pektrew</h1>
    <p class="person__title">Creative Director</p>
    <div class="divider"></div>
    <ul class="contact">
      <li class="contact__item">
        <svg class="contact__icon" viewBox="0 0 12 12" aria-hidden="true"><path fill="#f4eef2" d="M2.3 0.8l1.8 0 .8 2.6-1.2 1c.6 1.4 1.6 2.4 3 3l1-1.2 2.6.8 0 1.8c0 .6-.5 1.1-1.1 1.1C5 9.9 2.1 7 2 2 2 1.3 1.7.8 2.3.8z"/></svg>
        <span>(04) 5550 1928</span>
      </li>
      <li class="contact__item">
        <svg class="contact__icon" viewBox="0 0 12 12" aria-hidden="true"><rect x="0.5" y="2.5" width="11" height="7.5" fill="#f4eef2"/><path d="M0.8 2.8 6 7 11.2 2.8M0.8 9.8 4.5 6M11.2 9.8 7.5 6" fill="none" stroke="#2c1224" stroke-width="0.9"/></svg>
        <span>Rosalind@galaswithwren.example</span>
      </li>
      <li class="contact__item">
        <svg class="contact__icon" viewBox="0 0 12 12" aria-hidden="true"><g fill="none" stroke="#f4eef2" stroke-width="0.9"><circle cx="6" cy="6" r="5"/><ellipse cx="6" cy="6" rx="2.2" ry="5"/><path d="M1 6h10M1.8 3.5h8.4M1.8 8.5h8.4"/></g></svg>
        <span>www.galaswithwren.example</span>
      </li>
    </ul>
  </section>
</main>
</body>
</html>
```